Global Weight loss program

we need a business card based in Brooklyn , NY called PeppertonRUN . Mara Dulvik Tenbrook the founder and creator of PeppertonRUN Movement. A business based around nutrition, health, Whole Foods and fitness.

Industry/Entity Type

Food Service

Contact Information for Business Card

Phone number : 718-555-0143
website www.peppertonrun.com
email : mara@peppertonrun.com

Font styles to use
Sans Serif

Requirements
Must have
• logo colors
• green black and gold
Nice to have
• must be simple and sharp.
Should not have
• pictures of items

```html
<!DOCTYPE html>
<html lang="en">
<head>
<meta charset="utf-8">
<title>PeppertonRUN Business Card</title>
<link rel="stylesheet" href="https://fonts.googleapis.com/css2?family=Arimo:wght@400;700&family=Montserrat:wght@600&family=Cinzel:wght@400&display=swap">
<style>
  :root {
    --gold: #cfac5e;
    --white: #ffffff;
    --paper: #fcfcfc;
    --ink: #333333;
    --ink-soft: #555555;
    --green: #7cc242;
    --icon-bg: #111111;
  }
  html, body {
    margin: 0;
    padding: 0;
    overflow: hidden;
    background: var(--white);
  }
  .canvas {
    position: relative;
    width: 1200px;
    height: 1183px;
    overflow: hidden;
    background: var(--white);
  }
  .card-front, .card-back {
    position: absolute;
    left: 0;
    width: 1200px;
  }
  .card-front { top: 0; height: 563px; }
  .card-back { top: 619px; height: 564px; }
  .card-shape { position: absolute; inset: 0; display: block; }

  .brand {
    position: absolute;
    left: 0;
    width: 1200px;
    top: 300px;
    text-align: center;
  }
  .brand-name {
    display: inline-flex;
    align-items: center;
    gap: 14px;
    font-family: "Montserrat", sans-serif;
    font-weight: 600;
    font-size: 62px;
    letter-spacing: -1px;
    color: var(--ink);
    line-height: 1;
  }
  .brand-mark {
    width: 30px;
    height: 30px;
    background: var(--green);
  }
  .brand-tagline {
    margin-top: 12px;
    font-family: "Arimo", sans-serif;
    font-size: 19px;
    letter-spacing: 2.5px;
    color: var(--ink-soft);
  }

  .holder {
    position: absolute;
    left: 25px;
    top: 236px;
  }
  .holder-salutation {
    font-family: "Cinzel", serif;
    font-size: 66px;
    color: var(--ink);
    line-height: 1;
    letter-spacing: -3px;
  }
  .holder-title {
    position: absolute;
    left: 124px;
    top: 62px;
    font-family: "Arimo", sans-serif;
    font-size: 36px;
    color: var(--ink);
    white-space: nowrap;
  }

  .contacts {
    position: absolute;
    left: 680px;
    top: 128px;
    margin: 0;
    padding: 0;
    list-style: none;
  }
  .contact-item {
    display: flex;
    align-items: center;
    height: 75px;
    margin-bottom: 37px;
  }
  .contact-icon {
    width: 75px;
    height: 75px;
    flex: none;
    background: var(--icon-bg);
  }
  .contact-text {
    margin-left: 29px;
    font-family: "Arimo", sans-serif;
    font-weight: 700;
    font-size: 31px;
    color: var(--ink);
  }
</style>
</head>
<body>
<main class="canvas">

  <section class="card-front">
    <svg class="card-shape" width="1200" height="563" viewBox="0 0 1200 563">
      <rect width="1200" height="563" fill="var(--gold)"/>
      <polygon points="600,-60 943,282 600,625 257,282" fill="var(--white)"/>
    </svg>
    <div class="brand">
      <div class="brand-name"><span class="brand-mark"></span>PeppertonRUN</div>
      <div class="brand-tagline">Fitness, Nutrition and Health</div>
    </div>
  </section>

  <section class="card-back">
    <svg class="card-shape" width="1200" height="564" viewBox="0 0 1200 564">
      <rect width="1200" height="564" fill="var(--paper)"/>
      <polygon points="0,0 761,0 496,282 761,564 0,564" fill="var(--gold)"/>
    </svg>

    <div class="holder">
      <div class="holder-salutation">MR.</div>
      <div class="holder-title">President</div>
    </div>

    <ul class="contacts">
      <li class="contact-item">
        <svg class="contact-icon" viewBox="0 0 75 75" aria-hidden="true">
          <rect width="75" height="75" fill="var(--icon-bg)"/>
          <path d="M24 20 l7 -2 l5 10 l-4 4 q3 8 10 12 l4 -4 l10 5 l-2 7 q-4 4 -10 2 q-18 -7 -22 -24 q-1 -6 2 -10z" fill="none" stroke="#fff" stroke-width="2.5" stroke-linejoin="round"/>
          <path d="M42 22 a10 10 0 0 1 10 10 M42 15 a17 17 0 0 1 17 17" fill="none" stroke="#fff" stroke-width="2.5" stroke-linecap="round"/>
        </svg>
        <span class="contact-text">718-555-0143</span>
      </li>
      <li class="contact-item">
        <svg class="contact-icon" viewBox="0 0 75 75" aria-hidden="true">
          <rect width="75" height="75" fill="var(--icon-bg)"/>
          <g fill="none" stroke="#fff" stroke-width="2">
            <circle cx="37.5" cy="37.5" r="20"/>
            <ellipse cx="37.5" cy="37.5" rx="9" ry="20"/>
            <line x1="37.5" y1="17.5" x2="37.5" y2="57.5"/>
            <line x1="20" y1="28" x2="55" y2="28"/>
            <line x1="20" y1="47" x2="55" y2="47"/>
          </g>
          <rect x="21" y="32" width="33" height="11" fill="var(--icon-bg)"/>
          <text x="37.5" y="41" text-anchor="middle" font-family="Arimo, sans-serif" font-size="9" font-weight="700" fill="#fff">WWW</text>
        </svg>
        <span class="contact-text">www.peppertonrun.com</span>
      </li>
      <li class="contact-item">
        <svg class="contact-icon" viewBox="0 0 75 75" aria-hidden="true">
          <rect width="75" height="75" fill="var(--icon-bg)"/>
          <g fill="none" stroke="#fff" stroke-width="2.2" stroke-linejoin="round">
            <path d="M17 32 l20.5 -14 l20.5 14 v25 h-41z"/>
            <path d="M17 57 l16 -13 M58 57 l-16 -13"/>
            <path d="M24 37 v-12 h27 v12"/>
          </g>
          <text x="37.5" y="36" text-anchor="middle" font-family="Arimo, sans-serif" font-size="11" font-weight="700" fill="#fff">@</text>
        </svg>
        <span class="contact-text">mara@peppertonrun.com</span>
      </li>
    </ul>
  </section>

</main>
</body>
</html>
```